Business Card Design

Just looking for a good designs that looks good with our company logo. I'd like it to be simple and to the point. Just including contact information, our logo, and my name somewhere on the card so future clients know who they're contacting, and a couple services offered. The two images I attached are pictures of our logo. I don't care which color they they are, I just attached both images to give a reference of logo colors depending on the color of the card.
Names: Calvin Prewitt
Phone: 555-247-9061
Email: tidyturfcrew@mailvista.net
Services offered:
Mowing
Fertilization
Aeration
Bed & tree maintenance
and more.
Industry/Entity Type
Business
Contact Information for Business Card
Names: Calvin Prewitt
Phone: 555-247-9061
Look and feel

```html
<!DOCTYPE html>
<html lang="en">
<head>
<meta charset="utf-8">
<title>Tidy Turf – Business Card</title>
<link rel="stylesheet" href="https://fonts.googleapis.com/css2?family=Arimo:wght@400;700&family=Montserrat:wght@600&display=swap">
<style>
  :root {
    --page-bg: #e4e4e4;
    --card-bg: #2f3034;
    --accent: #e8523f;
    --text-light: #ffffff;
  }
  * { margin: 0; padding: 0; box-sizing: border-box; }
  html, body {
    width: 1200px;
    height: 1199px;
    overflow: hidden;
    background: var(--page-bg);
  }
  .business-card {
    position: absolute;
    left: 60px;
    top: 284px;
    width: 1080px;
    height: 631px;
    background: var(--card-bg);
    font-family: "Arimo", Arial, sans-serif;
    color: var(--text-light);
  }
  .brand {
    position: absolute;
    left: 78px;
    top: 150px;
    display: flex;
    align-items: center;
    gap: 22px;
  }
  .brand-dot {
    width: 86px;
    height: 86px;
    border-radius: 50%;
    background: var(--accent);
  }
  .brand-name {
    font-family: "Arimo", Arial, sans-serif;
    font-weight: 700;
    font-size: 58px;
    letter-spacing: 1px;
    color: var(--text-light);
  }
  .services {
    position: absolute;
    right: 79px;
    top: 112px;
    list-style: none;
    text-align: right;
    color: var(--accent);
    font-size: 24px;
    line-height: 33px;
  }
  .contact {
    position: absolute;
    right: 79px;
    top: 436px;
    text-align: right;
  }
  .contact-name {
    font-family: "Montserrat", "Century Gothic", sans-serif;
    font-weight: 600;
    font-size: 33px;
    letter-spacing: 0.5px;
    margin-bottom: 27px;
  }
  .contact-line {
    font-size: 22px;
    line-height: 30px;
  }
</style>
</head>
<body>
  <div class="business-card">
    <div class="brand">
      <span class="brand-dot"></span>
      <span class="brand-name">Tidy Turf</span>
    </div>

    <ul class="services">
      <li>Mowing</li>
      <li>Fertilization</li>
      <li>Aeration</li>
      <li>Bed &amp; tree maintenance</li>
      <li>and more.</li>
    </ul>

    <div class="contact">
      <p class="contact-name">Calvin Prewitt</p>
      <p class="contact-line">555-247-9061</p>
      <p class="contact-line">tidyturfcrew@mailvista.net</p>
    </div>
  </div>
</body>
</html>
```